Ferncrest Dental, LLC business card project

Business card to be designed with current logo.
Dental office- please keep design of card that looks clean and professional.
Please include the following info:
Ferncrest Dental, LLC
Dr. Lorna Pettigrew
2871 Marlowe Street
Bethlehem, PA 18093
610-555-0193
ferncrestdental.office@examplemail.test
Hello everyone-
Reason: Just got back from overseas- will look at all designs and provide feedback. Thank you!
Reason: Polling my friends for the final selection-
thank you to all those that participated- so many talented designers!

```html
<!DOCTYPE html>
<html lang="en">
<head>
<meta charset="utf-8">
<title>Ferncrest Dental, LLC — Business Card</title>
<link rel="stylesheet" href="https://fonts.googleapis.com/css2?family=Gelasio:wght@400&display=swap">
<style>
  :root {
    --card-bg: #ffffff;
    --frame: #000000;
    --ink: #111111;
    --brand-green: #5cc31a;
    --accent-green: #5ab05e;
    --accent-blue: #0a14f5;
  }
  html, body {
    margin: 0;
    padding: 0;
    width: 1200px;
    height: 589px;
    overflow: hidden;
    background: var(--card-bg);
  }
  .card {
    position: relative;
    box-sizing: border-box;
    width: 1200px;
    height: 589px;
    border: 3px solid var(--frame);
    background: var(--card-bg);
    font-family: "Gelasio", Georgia, serif;
    color: var(--ink);
  }
  .side-strip {
    position: absolute;
    top: 0;
    bottom: 0;
    width: 52px;
    background: linear-gradient(180deg,
      var(--accent-green) 0%, var(--accent-blue) 14%, var(--accent-green) 28%,
      var(--accent-blue) 42%, var(--accent-green) 56%, var(--accent-blue) 70%,
      var(--accent-green) 84%, var(--accent-blue) 100%);
    opacity: 0.85;
  }
  .side-strip--left { left: 4px; }
  .side-strip--right { right: 4px; }
  .brand {
    position: absolute;
    top: 22px;
    left: 0;
    right: 0;
    display: flex;
    justify-content: center;
    align-items: center;
    gap: 22px;
  }
  .brand__mark {
    width: 56px;
    height: 56px;
    border-radius: 50%;
    background: var(--brand-green);
  }
  .brand__name {
    margin: 0;
    font-size: 72px;
    font-weight: 400;
    line-height: 1.3;
    color: var(--brand-green);
  }
  .contact {
    position: absolute;
    top: 176px;
    left: 0;
    right: 0;
    text-align: center;
  }
  .contact__name {
    margin: 0 0 22px;
    font-size: 39px;
    font-weight: 400;
    line-height: 1.2;
  }
  .contact__line {
    margin: 0 0 40px;
    font-size: 23px;
    line-height: 1.3;
  }
  .contact__line:last-child { margin-bottom: 0; }
</style>
</head>
<body>
  <div class="card">
    <div class="side-strip side-strip--left" role="img" aria-label="Decorative border of alternating green circles and blue diamonds"></div>
    <div class="side-strip side-strip--right" role="img" aria-label="Decorative border of alternating green circles and blue diamonds"></div>

    <header class="brand">
      <span class="brand__mark" aria-hidden="true"></span>
      <h1 class="brand__name">Ferncrest Dental, LLC</h1>
    </header>

    <section class="contact">
      <p class="contact__name">Dr. Lorna Pettigrew</p>
      <p class="contact__line">2871 Marlowe Street</p>
      <p class="contact__line">Bethlehem, PA 18093</p>
      <p class="contact__line">610-555-0193</p>
    </section>
  </div>
</body>
</html>
```